Ski and Snowboard Instructor Business card

An eye catching business card capturing the essence of the sport and the mountain with a professional finish and easily readable contact information.

Notes on uploaded files:
I must have the KORVE (Northern Guild of Alpine Coaching Standards) Logo featured on the design (I designed it on the front but you can move if you think it would look better else where). The front of the card as you will see is a picture of a mountain top, if you can find a real image of this with a clear blue sky and snow that would be great -even better if it was from New Zealand as that is where I will be using the card!!! but also I am open to creative ones - logo style, 2D mountain outline etc.
As for the back something clean and simple, I originally designed it as matt black background with stylised writing for my name and a contrasting colour for the other writing. Possibly add the tag line 'certified snowsports instructor' I didn't just because of spacing etc but I'm keen to see what you guys come up with.

Writing on the back
Jamie Whitcombe
SKI - SNOWBOARD
jamiewhitcombe2008@frostmail.example
NZ: 02107481639
UK: (+44) 07835519402
Hope this helps
Happy designing!

Industry/Entity Type

Business

Contact Information for Business Card

See description

Requirements
Must have
• KORVE (Northern guild of Alpine Coaching Standards) logo. It is a trademarked logo so please no alterations in shape or colour.
Nice to have
• Real Images of mountains, snow etc

```html
<!DOCTYPE html>
<html lang="en">
<head>
<meta charset="utf-8">
<title>Jamie Whitcombe — Ski &amp; Snowboard Instructor Business Card</title>
<link rel="stylesheet" href="https://fonts.googleapis.com/css2?family=Parisienne&family=Cormorant+Garamond:wght@600&display=swap">
<style>
  :root {
    --backdrop: #e7e7e4;
    --sky-top: #3c78c0;
    --sky-low: #a9c9ea;
    --ridge: #4d6a9a;
    --snow: #e9eff7;
    --ice: #aebfd6;
    --logo-navy: #1f3a78;
    --name-light: #ffffff;
    --mono-light: #f3f3f3;
    --mono-mid: #c9c9c9;
    --mono-dark: #a2a2a2;
    --ink: #1d1d1d;
  }
  * { box-sizing: border-box; margin: 0; padding: 0; }
  html, body {
    width: 1200px; height: 871px; overflow: hidden;
    background: var(--backdrop);
  }
  .sheet {
    position: relative; width: 1200px; height: 871px;
    display: flex; flex-direction: column; align-items: center; justify-content: center;
    gap: 44px;
  }
  .card {
    position: relative; width: 560px; height: 320px;
    overflow: hidden;
    box-shadow: 0 6px 18px rgba(0,0,0,.25);
  }
  /* Front */
  .card--front .photo {
    position: absolute; inset: 0;
    background: linear-gradient(180deg,
      var(--sky-top) 0%,
      var(--sky-low) 42%,
      var(--ridge) 58%,
      var(--ice) 72%,
      var(--snow) 84%,
      var(--ice) 100%);
  }
  .brand {
    position: absolute; left: 24px; top: 36px;
    display: flex; align-items: center; gap: 8px;
  }
  .brand__mark { width: 22px; height: 22px; background: var(--logo-navy); }
  .brand__name {
    font-family: "Cormorant Garamond", serif; font-weight: 600;
    font-size: 30px; letter-spacing: 1px; color: var(--logo-navy); line-height: 1;
  }
  .front-name {
    position: absolute; left: 240px; top: 26px;
    font-family: "Parisienne", cursive; font-weight: 400; font-size: 46px; line-height: 1.05;
    color: var(--name-light);
    text-shadow: 0 1px 3px rgba(30,50,90,.5);
  }
  .front-name span { display: block; }
  .front-name span + span { margin-left: 40px; }
  /* Back */
  .card--back .photo {
    position: absolute; inset: 0;
    background: linear-gradient(170deg,
      var(--mono-light) 0%,
      #e2e2e2 40%,
      var(--mono-mid) 70%,
      var(--mono-dark) 100%);
  }
  .details {
    position: absolute; left: 220px; top: 56px; width: 320px;
    color: var(--ink);
  }
  .details__name {
    font-family: "Parisienne", cursive; font-weight: 400; font-size: 36px; line-height: 1.1;
  }
  .details__role {
    font-family: "Cormorant Garamond", serif; font-weight: 600;
    font-size: 16px; letter-spacing: 1.5px; margin: 8px 0 14px 48px;
  }
  .details__contact {
    font-family: "Parisienne", cursive; font-size: 19px; line-height: 1.4;
    list-style: none;
  }
  .details__contact li:first-child { font-size: 17px; }
</style>
</head>
<body>
<main class="sheet">
  <section class="card card--front">
    <div class="photo" role="img" aria-label="Photograph of a snow-covered mountain peak under a clear blue sky"></div>
    <div class="brand">
      <span class="brand__mark"></span>
      <span class="brand__name">KORVE</span>
    </div>
    <h1 class="front-name"><span>Jamie</span><span>Whitcombe</span></h1>
  </section>

  <section class="card card--back">
    <div class="photo" role="img" aria-label="Faded black and white photograph of snowy mountain summits"></div>
    <div class="details">
      <h2 class="details__name">Jamie Whitcombe</h2>
      <p class="details__role">SKI · SNOWBOARD</p>
      <ul class="details__contact">
        <li>jamiewhitcombe2008@frostmail.example</li>
        <li>NZ: 02107481639</li>
        <li>UK: (+44) 07835519402</li>
      </ul>
    </div>
  </section>
</main>
</body>
</html>
```